Extend Medium Rectangle into Halfpage and Billboard Ad Format

We have a few variations of our Medium Rectangle (300x250) that we use to build scalable online ads for local advertisers based on their images and logos which in most of the cases are very basic but still should deliver decent results in terms of overall banner look.

Based on those variations we would like to have each a Halfpage and Billboard variation to it that resembles the "look & feel" to feel like "out of one hand" and allows the local advertiser to recognize his ad across all formats.

Core of the Medium Rectangle is a carousel ad to swipe through the images and "more information" for the click-out to the landingpage. That might be great to replicate on the other banner formats but also could be done differently.

Attached the examples we have for one local customer to build ads from. Very limited but realistic.

```html
<!DOCTYPE html>
<html lang="de">
<head>
<meta charset="utf-8">
<title>Gasthof Linde – Billboard</title>
<link rel="stylesheet" href="https://fonts.googleapis.com/css2?family=Cinzel:wght@500&family=PT+Serif&display=swap">
<style>
  :root {
    --maroon: #5a1418;
    --maroon-deep: #4a0f12;
    --gold: #e3a21c;
    --gold-light: #f0c04a;
    --gold-dark: #a8650c;
    --white: #ffffff;
    --ink: #2a1406;
  }
  html, body {
    margin: 0;
    padding: 0;
    overflow: hidden;
    background: var(--maroon);
  }
  .billboard {
    position: relative;
    width: 1200px;
    height: 309px;
    overflow: hidden;
    background: linear-gradient(90deg, var(--maroon-deep) 0%, var(--maroon) 45%, var(--maroon) 100%);
  }
  .billboard__art {
    position: absolute;
    inset: 0;
  }
  .brand-name {
    position: absolute;
    left: 564px;
    top: 155px;
    transform: translate(-50%, -50%);
    margin: 0;
    font-family: "Cinzel", serif;
    font-weight: 500;
    font-size: 60px;
    letter-spacing: 1px;
    color: var(--white);
  }
  .headline {
    position: absolute;
    left: 972px;
    top: 92px;
    transform: translateX(-50%);
    margin: 0;
    width: 400px;
    text-align: center;
    font-family: "PT Serif", serif;
    font-weight: 400;
    font-size: 28px;
    line-height: 1.33;
    color: var(--white);
  }
  .cta {
    position: absolute;
    left: 873px;
    top: 202px;
    width: 198px;
    height: 39px;
    box-sizing: border-box;
    display: flex;
    align-items: center;
    justify-content: center;
    border-radius: 4px;
    border: 1px solid var(--gold-dark);
    background: linear-gradient(180deg, var(--gold-light) 0%, var(--gold) 50%, var(--gold-dark) 100%);
    font-family: "PT Serif", serif;
    font-size: 21px;
    color: var(--ink);
    text-decoration: none;
  }
</style>
</head>
<body>
  <div class="billboard">
    <svg class="billboard__art" width="1200" height="309" viewBox="0 0 1200 309" aria-hidden="false">
      <defs>
        <linearGradient id="photo-tones" x1="0" y1="0" x2="0" y2="1">
          <stop offset="0" stop-color="#cfe0ee"/>
          <stop offset="0.3" stop-color="#b86a52"/>
          <stop offset="0.45" stop-color="#e6e0b6"/>
          <stop offset="0.8" stop-color="#d9d1a6"/>
          <stop offset="1" stop-color="#8e8a78"/>
        </linearGradient>
      </defs>
      <path class="frame-band" d="M0 0 H362 Q420 154 362 309 H0 Z" fill="var(--gold)"/>
      <path class="photo-area" role="img" aria-label="Foto: Fassade des Gasthofs mit Sonnenschirm und Blumen im Vordergrund"
            d="M0 0 H350 Q406 154 350 309 H0 Z" fill="url(#photo-tones)"/>
    </svg>

    <p class="brand-name">LINDE</p>

    <h1 class="headline">Neueroffnung Gasthof<br>Linde in Bergwiesen</h1>

    <a class="cta" href="#">Mehr erfahren</a>
  </div>
</body>
</html>
```